Dental office needs a newspaper ad to encourage new patients to join our practice

"October Teeth Whitening Special" Call today to schedule your next dental cleaning and exam and receive a free bleach kit. (small disclaimer at the bottom of the ad) Dr. Pelton and his staff follow the most up-to-date NHQ infection control guidelines to protect our patients from CoVid-19 exposure. We offer a full spectrum of dental services including oral surgery, implants, root canals and cosmetic crowns and bridges. Our staff of licensed dental hygienists provide continued periodontal care for the healthiest teeth and gums. Visit our website. These are just some ideas you might be able to use. Also mention that most insurances are accepted. Emergencies and new patients welcome. As softer southern style motif like in our website can be used as a backdrop. The color scheme of the business logo and stationery is the same as the website.
Target Market(s)
All ages, local population 8,000 southern farming community. White Hispanic older population. Not oriented towards children.
Requirements
Must have
- Nice color. See our website at peltondentalcare.example for basic image of practice
Nice to have
- It will be a quarter to half page in a local newspaper, so it can be good sized with plenty of print an graphics

```html
<!DOCTYPE html>
<html lang="en">
<head>
<meta charset="utf-8">
<title>October Teeth Whitening Special – Warren E. Pelton, DMD</title>
<link rel="stylesheet" href="https://fonts.googleapis.com/css2?family=Montserrat:wght@400;500;600;700;800&display=swap">
<style>
  :root {
    --sky: #c6e9f7;
    --navy: #0b63ad;
    --title: #0e5ea8;
    --sub: #1b5799;
    --teal: #7fd0c3;
    --tagline: #1f80cc;
    --ink: #1b1d2b;
    --white: #ffffff;
  }
  * { margin: 0; padding: 0; box-sizing: border-box; }
  html, body { width: 849px; height: 1200px; overflow: hidden; background: var(--white); }
  body { font-family: "Montserrat", sans-serif; }
  .ad { position: relative; width: 849px; height: 1200px; background: var(--sky); overflow: hidden; }
  .ad > * { position: absolute; }

  .hero-photo {
    left: 430px; top: 0; width: 419px; height: 403px;
    background: linear-gradient(90deg, rgba(198,233,247,1) 0%, rgba(160,205,225,0.6) 25%, #5b7fa0 60%, #1d2c4a 100%);
  }
  .headline {
    left: 52px; top: 46px; color: var(--title);
    font-weight: 800; font-size: 48px; line-height: 49px; letter-spacing: -1.5px;
    text-transform: uppercase;
  }
  .offer {
    left: 52px; top: 261px; color: var(--sub); white-space: nowrap;
    font-weight: 500; font-size: 22px; line-height: 29px;
  }
  .offer strong { font-weight: 800; }

  .info-band { left: 0; top: 485px; width: 849px; height: 322px; background: var(--navy); }

  .thumb {
    top: 370px; width: 226px; height: 175px;
    border: 7px solid var(--teal); border-radius: 14px;
  }
  .thumb-shades { left: 52px; background: linear-gradient(135deg, #f3d2cf, #ffffff 55%, #8b8b8b); }
  .thumb-implant { left: 316px; background: linear-gradient(135deg, #f6e4e0, #ffffff 50%, #a6dfe6); }
  .thumb-light { left: 577px; background: linear-gradient(135deg, #dff0fa, #b8d4ec 55%, #f1d8c8); }

  .about {
    left: 61px; top: 573px; color: var(--white); white-space: nowrap;
    font-size: 17px; line-height: 21.5px; font-weight: 400;
  }
  .perks { left: 417px; top: 579px; list-style: none; color: var(--white); font-weight: 700; font-size: 15.2px; line-height: 21.8px; }
  .perks li { display: flex; align-items: center; gap: 7px; white-space: nowrap; }
  .perks svg { flex: none; }

  .team-photo {
    left: 415px; top: 689px; width: 403px; height: 245px;
    background: var(--white); padding: 5px;
  }
  .team-photo div { width: 100%; height: 100%; background: linear-gradient(180deg, #d9cf9a 0%, #5cc0d8 45%, #4a6a3c 100%); }

  .assurance { left: 62px; top: 825px; list-style: none; color: var(--sub); font-weight: 800; font-size: 17.5px; line-height: 21.5px; text-transform: uppercase; }
  .assurance li { display: flex; align-items: center; gap: 13px; margin-bottom: 14px; white-space: nowrap; }

  .tagline {
    left: 0; top: 951px; width: 849px; text-align: center;
    color: var(--tagline); font-weight: 500; font-size: 25px; letter-spacing: 0.2px;
  }

  .footer { left: 0; top: 998px; width: 849px; height: 202px; background: var(--white); }
  .footer-rule { left: 0; top: 1193px; width: 849px; height: 7px; background: var(--navy); }

  .practice-mark { left: 70px; top: 1030px; width: 96px; height: 96px; border-radius: 50%; background: var(--navy); }
  .practice-name {
    left: 203px; top: 1029px; color: var(--navy);
    font-size: 43px; font-weight: 800; letter-spacing: -0.5px; white-space: nowrap;
  }
  .practice-name span { font-weight: 400; }

  .booking {
    left: 194px; top: 1101px; width: 529px; height: 47px; border-radius: 24px;
    background: var(--navy); color: var(--white);
    display: flex; align-items: center;
  }
  .booking-label { width: 235px; text-align: center; font-weight: 700; font-size: 16px; line-height: 16.5px; }
  .booking-phone { display: flex; align-items: center; gap: 12px; font-weight: 700; font-size: 32px; white-space: nowrap; }

  .contacts {
    left: 27px; top: 1160px; width: 794px; display: flex; align-items: center; justify-content: space-between;
    color: var(--ink); font-weight: 700; font-size: 14.2px; white-space: nowrap;
  }
  .contacts span { display: flex; align-items: center; gap: 7px; }
</style>
</head>
<body>
<main class="ad">
  <div class="hero-photo" role="img" aria-label="Dentist in gloves treating a smiling patient in the dental chair"></div>

  <h1 class="headline">October<br>Teeth<br>Whitening<br>Special</h1>
  <p class="offer">Call today to schedule your next<br>dental cleaning and exam and receive<br>a <strong>FREE</strong> bleach kit.</p>

  <div class="info-band"></div>

  <div class="thumb thumb-shades" role="img" aria-label="Bright smile beside a tooth shade guide"></div>
  <div class="thumb thumb-implant" role="img" aria-label="Smiling woman holding a dental implant model"></div>
  <div class="thumb thumb-light" role="img" aria-label="Patient in protective glasses receiving a whitening light treatment"></div>

  <p class="about">Dr. Pelton and his staff follow the<br>most up-to-date NHQ infection control<br>guidelines to protect our patients<br>from CoVid-19 exposure. We offer a full<br>spectrum of dental services including<br>oral surgery, implants, root canals and<br>cosmetic crowns and bridges. Our staff<br>of licensed dental hygienists provide<br>continued periodontal care for the<br>healthiest teeth and gums.</p>

  <ul class="perks">
    <li><svg width="14" height="10" viewBox="0 0 14 10"><path d="M1 5l4 3 8-7" fill="none" stroke="#7fd0f0" stroke-width="2.6" stroke-linecap="round"/></svg>Over 30 years of combined experience</li>
    <li><svg width="14" height="10" viewBox="0 0 14 10"><path d="M1 5l4 3 8-7" fill="none" stroke="#7fd0f0" stroke-width="2.6" stroke-linecap="round"/></svg>We offer many dental services and restoration</li>
    <li><svg width="14" height="10" viewBox="0 0 14 10"><path d="M1 5l4 3 8-7" fill="none" stroke="#7fd0f0" stroke-width="2.6" stroke-linecap="round"/></svg>We provide a warm and caring environment</li>
    <li><svg width="14" height="10" viewBox="0 0 14 10"><path d="M1 5l4 3 8-7" fill="none" stroke="#7fd0f0" stroke-width="2.6" stroke-linecap="round"/></svg>We have Caring And Experienced Staff</li>
  </ul>

  <div class="team-photo"><div role="img" aria-label="Dental team in scrubs and white coats standing outside the practice"></div></div>

  <ul class="assurance">
    <li><svg width="40" height="40" viewBox="0 0 40 40"><circle cx="20" cy="20" r="18" fill="#ffffff" stroke="#a9e3f2" stroke-width="2.5"/><path d="M12 20l6 6 10-12" fill="none" stroke="#3cb4e0" stroke-width="4" stroke-linecap="round" stroke-linejoin="round"/></svg><span>All insurances<br>are accepted.</span></li>
    <li><svg width="40" height="40" viewBox="0 0 40 40"><circle cx="20" cy="20" r="18" fill="#ffffff" stroke="#a9e3f2" stroke-width="2.5"/><path d="M12 20l6 6 10-12" fill="none" stroke="#3cb4e0" stroke-width="4" stroke-linecap="round" stroke-linejoin="round"/></svg><span>Emergencies and new<br>patients welcome.</span></li>
  </ul>

  <p class="tagline">COMPLETE DENTAL CARE FOR YOU &amp; YOUR FAMILY</p>

  <div class="footer"></div>
  <div class="practice-mark"></div>
  <p class="practice-name">Warren E. Pelton, <span>DMD</span></p>

  <div class="booking">
    <div class="booking-label">BOOK YOUR<br>APPOINTMENT NOW</div>
    <div class="booking-phone">
      <svg width="30" height="30" viewBox="0 0 24 24"><path d="M6.6 3.5l2.6 3.2-1.6 2.2c1 2.2 2.9 4.3 5.5 5.5l2.2-1.6 3.2 2.6-1.4 2.9c-6.3-.3-12.1-6.1-12.4-12.4z" fill="none" stroke="#fff" stroke-width="1.6" stroke-linejoin="round"/><path d="M14 4a6 6 0 0 1 6 6M14 7a3 3 0 0 1 3 3" fill="none" stroke="#fff" stroke-width="1.6" stroke-linecap="round"/></svg>
      (555) 014-2287
    </div>
  </div>

  <div class="contacts">
    <span><svg width="20" height="15" viewBox="0 0 20 15"><rect x="1" y="1" width="18" height="13" fill="none" stroke="#0b63ad" stroke-width="2"/><path d="M1 2l9 7 9-7" fill="none" stroke="#0b63ad" stroke-width="2"/></svg>smiles@pelton.example</span>
    <span><svg width="14" height="20" viewBox="0 0 14 20"><path d="M7 19s6-7 6-11.5A6 6 0 0 0 1 7.5C1 12 7 19 7 19z" fill="none" stroke="#0b63ad" stroke-width="1.8"/><circle cx="7" cy="7.5" r="2.2" fill="none" stroke="#0b63ad" stroke-width="1.8"/></svg>12 Oak St, Riverton, FL 30000</span>
    <span><svg width="20" height="20" viewBox="0 0 20 20"><circle cx="10" cy="10" r="8.5" fill="none" stroke="#0b63ad" stroke-width="1.8"/><ellipse cx="10" cy="10" rx="3.8" ry="8.5" fill="none" stroke="#0b63ad" stroke-width="1.6"/><path d="M1.5 10h17" stroke="#0b63ad" stroke-width="1.6"/></svg>www.peltondentalcare.example</span>
  </div>

  <div class="footer-rule"></div>
</main>
</body>
</html>
```